Bref créative
Stand out Biz Cards & Stationery for Quarvenix
A Cutting Edge Consulting & Executive Coaching Firm
Simple
Torben K. Aldavisto, PhD
President & CEO
48207 E Corvane Ave
Suite 2875-417
Phoenix, AZ 85093-6718
Torben@Aldavisto-mail.test
www.Aldavisto-mail.test
It might be questionable to use the tag line in the Logo since the font is very tiny.
The significant problems we have, cannot be solved at the same level of thinking with which we created them. -- Gustav Merriwold

```html
<!DOCTYPE html>
<html lang="en">
<head>
<meta charset="utf-8">
<title>Quarvenix Stationery</title>
<link href="https://fonts.googleapis.com/css2?family=Arimo:ital,wght@0,400;0,700;1,400&display=swap" rel="stylesheet">
<style>
:root{
  --bronze-dark:#6e4323;
  --bronze-mid:#b0784a;
  --bronze-light:#d9a77a;
  --blue-deep:#17338c;
  --blue:#2a55b8;
  --blue-light:#5b8ee0;
  --ink:#3a3a3a;
  --paper:#ffffff;
  --muted:#8a8a8a;
}
*{box-sizing:border-box;margin:0;padding:0}
html,body{width:1200px;height:607px;overflow:hidden}
body{
  position:relative;
  font-family:"Arimo",Arial,sans-serif;
  color:var(--ink);
  background:radial-gradient(ellipse at 60% 40%,var(--bronze-light) 0%,var(--bronze-mid) 45%,var(--bronze-dark) 100%);
}
.sheet{position:absolute;background:var(--paper);box-shadow:0 3px 8px rgba(0,0,0,.35);overflow:hidden}
.brand{font-family:"Arimo",Arial,sans-serif;font-weight:700;color:var(--blue-deep);letter-spacing:.5px;line-height:1}
.tagline{font-size:4.5px;letter-spacing:1.5px;color:var(--muted);text-transform:uppercase;margin-top:2px}

/* business card front */
.card-front{left:31px;top:19px;width:180px;height:103px}
.card-front .wave{position:absolute;inset:0}
.card-front .brand{position:absolute;left:10px;top:9px;font-size:17px}
.card-front .details{position:absolute;left:10px;top:38px;font-size:4.6px;line-height:6.2px;color:var(--ink)}
.card-front .name{font-weight:700;font-size:5.4px}
.card-front .gap{height:4px}

/* card backs */
.card-back{left:31px;width:180px;height:98px;display:flex;align-items:center;justify-content:center;text-align:center;padding:0 22px}
.card-back p{font-size:5.2px;line-height:7px;font-style:italic}
.card-back .author{display:block;font-style:normal;font-weight:700;color:var(--blue)}
.back-1{top:185px;color:var(--muted)}
.back-2{top:317px;background:linear-gradient(135deg,var(--blue-deep),var(--blue) 60%,var(--blue-light));color:#fff}
.back-2 .author{color:#fff}
.back-3{top:466px;color:var(--muted)}

/* letterhead */
.letterhead{left:233px;top:19px;width:401px;height:569px}
.letterhead .masthead{position:absolute;left:20px;top:14px}
.letterhead .brand{font-size:28px}
.letterhead .footer{position:absolute;left:0;right:0;bottom:14px;text-align:center;font-size:5.2px;color:var(--muted);letter-spacing:.2px}

/* envelope front */
.envelope{left:694px;top:19px;width:453px;height:259px}
.envelope .masthead{position:absolute;left:22px;top:20px}
.envelope .brand{font-size:30px}
.envelope .return{font-size:5.2px;color:var(--muted);margin-top:4px}

/* envelope back */
.envelope-back{left:694px;top:331px;width:453px;height:252px}
.envelope-back .flap{position:absolute;left:0;top:0;width:453px;height:62px}
.envelope-back .seal{position:absolute;left:219px;top:17px;width:15px;height:15px;border-radius:50%;background:#fff}
</style>
</head>
<body>

<section class="sheet card-front" aria-label="Business card front">
  <svg class="wave" viewBox="0 0 180 103" preserveAspectRatio="none" aria-hidden="true">
    <defs>
      <linearGradient id="cardWave" x1="0" y1="0" x2="1" y2="1">
        <stop offset="0" stop-color="#5b8ee0"/>
        <stop offset="1" stop-color="#17338c"/>
      </linearGradient>
    </defs>
    <path d="M140 0 C118 40 120 80 70 103 L180 103 L180 0 Z" fill="url(#cardWave)"/>
    <path d="M136 0 C114 40 116 80 64 103" fill="none" stroke="#9db8e8" stroke-width="1"/>
  </svg>
  <div class="brand">Quarvenix</div>
  <div class="details">
    <div class="name">Torben K. Aldavisto, PhD</div>
    <div>President &amp; CEO</div>
    <div class="gap"></div>
    <div>48207 E Corvane Ave</div>
    <div>Suite 2875-417</div>
    <div>Phoenix, AZ 85093-6718</div>
    <div class="gap"></div>
    <div>Torben@Aldavisto-mail.test</div>
    <div>www.Aldavisto-mail.test</div>
  </div>
</section>

<section class="sheet card-back back-1" aria-label="Business card back, white">
  <p>The significant problems we have, cannot be solved at the same level of thinking with which we created them. <span class="author">Gustav Merriwold</span></p>
</section>

<section class="sheet card-back back-2" aria-label="Business card back, blue">
  <p>The significant problems we have, cannot be solved at the same level of thinking with which we created them. <span class="author">Gustav Merriwold</span></p>
</section>

<section class="sheet card-back back-3" aria-label="Business card back, white alternate">
  <p>The significant problems we have, cannot be solved at the same level of thinking with which we created them. <span class="author">Gustav Merriwold</span></p>
</section>

<section class="sheet letterhead" aria-label="Letterhead">
  <div class="masthead">
    <div class="brand">Quarvenix</div>
    <div class="tagline">Consulting &amp; Coaching</div>
  </div>
  <div class="footer">48207 E Corvane Ave &nbsp;|&nbsp; Suite 2875-417 &nbsp;|&nbsp; Phoenix, AZ 85093-6718 &nbsp;|&nbsp; Torben@Aldavisto-mail.test &nbsp;|&nbsp; www.Aldavisto-mail.test</div>
</section>

<section class="sheet envelope" aria-label="Envelope front">
  <div class="masthead">
    <div class="brand">Quarvenix</div>
    <div class="tagline">Consulting &amp; Coaching</div>
    <div class="return">48207 E Corvane Ave · Suite 2875-417 · Phoenix, AZ 85093-6718</div>
  </div>
</section>

<section class="sheet envelope-back" aria-label="Envelope back">
  <svg class="flap" viewBox="0 0 453 62" preserveAspectRatio="none" aria-hidden="true">
    <defs>
      <linearGradient id="flapFill" x1="0" y1="0" x2="0" y2="1">
        <stop offset="0" stop-color="#5b8ee0"/>
        <stop offset="1" stop-color="#17338c"/>
      </linearGradient>
    </defs>
    <path d="M0 0 H453 V22 C420 34 380 50 226 56 C72 50 33 34 0 22 Z" fill="url(#flapFill)"/>
  </svg>
  <div class="seal"></div>
</section>

</body>
</html>
```